Finance Broker helping people meet their personal and business goals

New business card design,
1st look at the old business card so this makes sense.
I DON'T want:
the subtext "For all your Rural and Commercial Finance".
I DON'T want the: "and Management Consultant" words
I DON'T want the old phone: 07 48213957
I DON'T want the fax number: 07 45826031
I DON'T want the email address: tallowcreek@brightlink.com.au
I DON'T want the flower
What I DO want
I DO want the mobile 0451 836 209 (in larger text)
I DO want:
My name: Dennis Harwell-Lowe
I DO want: Australian Credit Licence 529164 (Tallow Creek Pty Ltd)
I DO want: Principal Finance Broker
I DO want new email: dennis@plotnextstep.com.au
I DO want address: PO Box 928, Tully Qld 4854
I DO want the existing logo (PNS on existing card)

Target Market(s)

Business Borrowers, Home Purchasers, and People wanting to finance cars and plant and equipment

Industry/Entity Type

Financial Service

Contact Information for Business Card

See project description

Font styles to use
Serif

Colors

Designer to choose colors to be used in the design.

Requirements
Must have
• See project description
Nice to have
• Black and Yellow colours
Should not have
• See project description

```html
<!DOCTYPE html>
<html lang="en">
<head>
<meta charset="utf-8">
<title>Plot Next Step – Business Card</title>
<link href="https://fonts.googleapis.com/css2?family=Tinos:wght@400;700&display=swap" rel="stylesheet">
<style>
  :root {
    --backdrop: #3b3b3b;
    --card: #1e1e1e;
    --accent: #dfe84c;
    --ink-light: #f2f2f2;
  }
  * { margin: 0; padding: 0; box-sizing: border-box; }
  html, body {
    width: 1200px;
    height: 960px;
    overflow: hidden;
    background: var(--backdrop);
    font-family: "Tinos", "Times New Roman", serif;
  }
  .stage {
    width: 1200px;
    height: 960px;
    display: flex;
    flex-direction: column;
    align-items: center;
    justify-content: center;
    gap: 50px;
  }
  .card {
    width: 700px;
    height: 400px;
    background: var(--card);
    border-radius: 22px;
    display: flex;
    flex-direction: column;
    align-items: center;
    justify-content: center;
    text-align: center;
    box-shadow: 0 10px 24px rgba(0,0,0,0.45);
  }
  .brand {
    display: flex;
    align-items: center;
    gap: 16px;
  }
  .brand-dot {
    border-radius: 50%;
    background: var(--accent);
    flex: none;
  }
  .brand-name {
    color: var(--accent);
    font-weight: 400;
    line-height: 1;
  }
  .card-front .brand-dot { width: 72px; height: 72px; }
  .card-front .brand-name { font-size: 54px; }

  .card-back .brand { margin-bottom: 22px; }
  .card-back .brand-dot { width: 44px; height: 44px; }
  .card-back .brand-name { font-size: 34px; }

  .holder-name {
    color: var(--accent);
    font-weight: 700;
    font-size: 34px;
    line-height: 1.1;
  }
  .holder-role,
  .licence,
  .email,
  .postal {
    color: var(--ink-light);
    font-size: 19px;
    line-height: 1.3;
  }
  .mobile {
    color: var(--accent);
    font-weight: 700;
    font-size: 32px;
    margin: 10px 0 4px;
    line-height: 1.1;
  }
</style>
</head>
<body>
<main class="stage">
  <section class="card card-front">
    <div class="brand">
      <span class="brand-dot"></span>
      <span class="brand-name">Plot Next Step</span>
    </div>
  </section>

  <section class="card card-back">
    <div class="brand">
      <span class="brand-dot"></span>
      <span class="brand-name">Plot Next Step</span>
    </div>
    <p class="holder-name">Dennis Harwell-Lowe</p>
    <p class="holder-role">Principal Finance Broker</p>
    <p class="licence">Australian Credit Licence 529164 (Tallow Creek Pty Ltd)</p>
    <p class="mobile">0451 836 209</p>
    <p class="email">Email: dennis@plotnextstep.com.au</p>
    <p class="postal">PO Box 928, Tully Qld 4854</p>
  </section>
</main>
</body>
</html>
```